RK Website Home Page Design

The task is to develop a winning design for a replacement website for our client RK Plumbing, Heating, AC & Remodeling. ct

```html
<!DOCTYPE html>
<html lang="en">
<head>
<meta charset="utf-8">
<title>RK Plumbing, Heating, AC &amp; Remodeling</title>
<link href="https://fonts.googleapis.com/css2?family=Outfit:wght@600;700&family=Poppins:wght@400;500;600&display=swap" rel="stylesheet">
<style>
:root{
  --navy:#1f3a6b;
  --navy-dark:#182f59;
  --yellow:#f9d800;
  --light:#f2f2f2;
  --white:#ffffff;
  --text:#2a2a2a;
  --border:#1f3a6b;
}
*{box-sizing:border-box;margin:0;padding:0}
html,body{width:1200px;height:4693px;overflow:hidden}
body{position:relative;font-family:'Poppins',sans-serif;color:var(--text);background:var(--light)}
.abs{position:absolute}
h1,h2,h3{font-family:'Outfit',sans-serif;font-weight:700;color:var(--navy);line-height:1.1}
.underline{position:absolute;height:3px;background:var(--yellow)}
.underline::before,.underline::after{content:"";position:absolute;top:-3px;width:9px;height:9px;border-radius:50%;background:var(--yellow)}
.underline::before{left:-4px}.underline::after{right:-4px}
.btn{position:absolute;display:flex;align-items:center;justify-content:center;border-radius:22px;font-size:12px;font-weight:600;letter-spacing:.5px;text-transform:uppercase}
.btn-yellow{background:var(--yellow);color:var(--navy)}
.btn-navy{background:var(--navy);color:var(--yellow)}
.img-fill{position:absolute}

/* header */
.header{position:absolute;left:0;top:0;width:1200px;height:133px;background:var(--white);z-index:2}
.topbar{position:absolute;left:319px;top:0;width:881px;height:49px;background:var(--navy);display:flex;align-items:center;gap:40px;padding-left:90px;color:#fff;font-size:11px}
.topbar span{display:flex;align-items:center;gap:14px}
.topbar .ic{width:24px;height:24px;border-radius:50%;background:var(--yellow);display:flex;align-items:center;justify-content:center}
.topbar .sep{width:1px;height:18px;background:#9fb0cf}
.logo{position:absolute;left:56px;top:26px;display:flex;align-items:center;gap:10px}
.logo .mark{width:26px;height:26px;border-radius:50%;background:var(--yellow)}
.logo .name{font-family:'Outfit',sans-serif;font-weight:700;font-size:30px;color:var(--navy)}
.nav{position:absolute;left:319px;top:82px;display:flex;gap:50px;font-size:11px;color:var(--navy);text-transform:uppercase}
.nav .active{font-weight:600}
.menu-btn{position:absolute;left:1037px;top:70px;width:42px;height:42px;border-radius:50%;background:var(--navy);display:flex;align-items:center;justify-content:center}

/* hero */
.hero{position:absolute;left:0;top:133px;width:1200px;height:682px;border-radius:0 0 40px 40px;background:linear-gradient(100deg,#243f72 0%,#2b4a80 55%,#3d5f94 100%);overflow:hidden}
.hero h1{position:absolute;left:126px;top:118px;font-size:50px;color:#fff;text-transform:uppercase;line-height:1.12}
.hero .underline{left:126px;top:285px;width:398px}
.checks{position:absolute;left:126px;top:314px;list-style:none;color:#fff;font-size:14px}
.checks li{display:flex;align-items:center;gap:32px;height:45.5px}
.hero .btn{left:125px;top:524px;width:167px;height:40px}
.form-card{position:absolute;left:673px;top:106px;width:402px;height:470px;background:#fff;border-radius:12px}
.form-card h2{position:absolute;left:0;width:100%;top:42px;text-align:center;font-size:34px;text-transform:uppercase}
.field{position:absolute;height:38px;border:1.5px solid var(--border);border-radius:20px;font-size:10px;color:#999;padding:12px 22px}
.field.area{height:178px;border-radius:18px}
.dots{position:absolute;left:1117px;top:283px}
.dots i{display:block;border-radius:50%;margin:0 auto 36px}

/* services */
.services{position:absolute;left:0;top:815px;width:1200px;height:562px;background:#fff;border-radius:0 0 40px 40px}
.center-title{position:absolute;left:0;width:1200px;text-align:center;text-transform:uppercase}
.services h2{top:97px;font-size:50px}
.services .underline{left:450px;top:213px;width:300px}
.svc{position:absolute;top:250px;width:144px;height:130px;border:1.5px solid var(--navy);border-radius:8px;background:#fff;display:flex;flex-direction:column;align-items:center;justify-content:center;gap:12px;font-size:11px;font-weight:600;color:var(--navy);text-align:center;text-transform:uppercase;line-height:1.3}
.svc.active{background:var(--yellow);border-color:var(--yellow);box-shadow:0 6px 16px rgba(0,0,0,.15)}
.arrow{position:absolute;width:32px;height:32px;border-radius:50%;display:flex;align-items:center;justify-content:center}
.arrow.dark{background:var(--navy)}
.arrow.light{background:#fff;box-shadow:0 2px 6px rgba(0,0,0,.15)}
.services .btn{left:517px;top:423px;width:167px;height:40px}

/* difference */
.difference{position:absolute;left:0;top:1377px;width:1200px;height:760px}
.difference h2{position:absolute;left:126px;top:100px;font-size:50px;text-transform:uppercase}
.difference .underline{left:126px;top:214px;width:150px}
.difference p{position:absolute;left:126px;top:240px;width:480px;font-size:12.5px;line-height:37.5px}
.difference .btn{left:126px;top:498px;width:166px;height:40px}
.circle-bg{position:absolute;left:675px;top:146px;width:414px;height:414px;border-radius:50%;background:#f6f0d6}

/* savings */
.savings{position:absolute;left:0;top:2137px;width:1200px;height:922px;background:var(--yellow);border-radius:40px}
.savings h2{top:97px;font-size:50px;line-height:1.1}
.savings .underline{left:480px;top:272px;width:240px;background:#a7a9c6}
.savings .underline::before,.savings .underline::after{background:#a7a9c6}
.deal{position:absolute;background:#fff;border-radius:14px;overflow:hidden}
.save{position:absolute;top:714px;left:450px;display:flex;align-items:center;gap:26px;color:var(--navy)}
.save b{font-family:'Outfit',sans-serif;font-size:20px}
.save .bar{width:1px;height:22px;background:#8a8a8a}
.save small{font-size:9.5px;line-height:1.3;text-transform:uppercase}
.savings .btn{left:480px;top:781px;width:240px;height:40px}

/* blog */
.blog{position:absolute;left:0;top:3059px;width:1200px;height:584px;background:#fff;border-radius:0 0 40px 40px}
.blog h2{position:absolute;left:126px;top:108px;font-size:50px;text-transform:uppercase}
.blog .underline{left:126px;top:168px;width:180px}
.blog .btn{left:908px;top:112px;width:167px;height:40px}
.post{position:absolute;top:233px;width:224px;height:250px;border-radius:8px;overflow:hidden}
.post .title{position:absolute;left:0;bottom:26px;width:100%;text-align:center;font-family:'Outfit',sans-serif;font-weight:700;font-size:19px;color:#fff;text-transform:uppercase}
.post.featured .title{bottom:auto;top:28px}
.post.featured p{position:absolute;left:20px;right:20px;top:76px;text-align:center;color:#fff;font-size:12.5px;line-height:37px}
.post.featured .more{position:absolute;left:0;width:100%;top:202px;text-align:center;font-size:12px;font-weight:600;color:var(--yellow)}

/* reminder */
.reminder{position:absolute;left:0;top:3643px;width:1200px;height:394px}
.reminder h2{top:88px;font-size:50px}
.reminder .underline{left:482px;top:186px;width:236px}
.reminder p{position:absolute;left:200px;width:800px;top:204px;text-align:center;font-size:12.5px;line-height:37.5px}

/* footer */
.footer{position:absolute;left:0;top:4037px;width:1200px;height:656px;background:var(--navy);border-radius:40px 40px 0 0;color:#fff}
.footer .logo{left:500px;top:140px}
.footer .logo .name{color:#fff}
.footer .about{position:absolute;left:122px;top:262px;width:300px;font-size:12.5px;line-height:42.5px}
.footer .vline{position:absolute;top:262px;width:1px;height:252px;background:#8a9dc0}
.footer .links{position:absolute;left:456px;top:250px;width:270px;list-style:none;text-align:center;font-size:12.5px;line-height:36px}
.footer .contact{position:absolute;left:770px;top:268px;font-size:12.5px;line-height:22px}
.footer .contact .row{display:flex;gap:24px;align-items:flex-start;margin-bottom:22px}
.footer .contact svg{flex:none;width:34px}
.footer .copy{position:absolute;left:0;width:1200px;top:622px;text-align:center;font-size:11.5px}
.footer .copyline{position:absolute;left:0;width:1200px;top:603px;height:1px;background:#3c5687}
</style>
</head>
<body>

<header class="header">
  <div class="logo"><span class="mark"></span><span class="name">RK Plumbing</span></div>
  <div class="topbar">
    <span><i class="ic"><svg width="12" height="9" viewBox="0 0 12 9"><rect x=".5" y=".5" width="11" height="8" fill="none" stroke="#1f3a6b"/><path d="M.5.5 6 5 11.5.5" fill="none" stroke="#1f3a6b"/></svg></i>www.rkheatingplumbing.com</span>
    <i class="sep"></i>
    <span><i class="ic"><svg width="12" height="12" viewBox="0 0 24 24"><path d="M6.6 10.8a15 15 0 0 0 6.6 6.6l2.2-2.2a1 1 0 0 1 1-.25 11 11 0 0 0 3.6.6 1 1 0 0 1 1 1V20a1 1 0 0 1-1 1A17 17 0 0 1 3 4a1 1 0 0 1 1-1h3.5a1 1 0 0 1 1 1 11 11 0 0 0 .6 3.6 1 1 0 0 1-.25 1z" fill="#1f3a6b"/></svg></i>555-310-2846</span>
    <i class="sep"></i>
    <span><i class="ic"><svg width="12" height="12" viewBox="0 0 24 24"><path d="M6.6 10.8a15 15 0 0 0 6.6 6.6l2.2-2.2a1 1 0 0 1 1-.25 11 11 0 0 0 3.6.6 1 1 0 0 1 1 1V20a1 1 0 0 1-1 1A17 17 0 0 1 3 4a1 1 0 0 1 1-1h3.5a1 1 0 0 1 1 1 11 11 0 0 0 .6 3.6 1 1 0 0 1-.25 1z" fill="#1f3a6b"/></svg></i>555-800-1937</span>
  </div>
  <nav class="nav"><span class="active">About</span><span>Plumbing</span><span>Water Heaters</span><span>Air Conditioning</span><span>Handy Work &amp; Remodeling</span></nav>
  <div class="menu-btn"><svg width="18" height="14" viewBox="0 0 18 14"><path d="M2 2h14M2 7h14M2 12h14" stroke="#f9d800" stroke-width="2"/></svg></div>
</header>

<section class="hero">
  <div class="img-fill" role="img" aria-label="Technician working on pipes, photo behind a navy overlay" style="inset:0;background:radial-gradient(circle at 85% 30%,rgba(120,150,200,.35),transparent 55%)"></div>
  <h1>Enjoy the best of<br>home living.<br>Indoors &amp; out.</h1>
  <div class="underline"></div>
  <ul class="checks">
    <li><svg width="14" height="12" viewBox="0 0 14 12"><path d="M1 6l4 4 8-9" fill="none" stroke="#f9d800" stroke-width="2.5"/></svg>Quick response</li>
    <li><svg width="14" height="12" viewBox="0 0 14 12"><path d="M1 6l4 4 8-9" fill="none" stroke="#f9d800" stroke-width="2.5"/></svg>Emergency &amp; Weekend Services</li>
    <li><svg width="14" height="12" viewBox="0 0 14 12"><path d="M1 6l4 4 8-9" fill="none" stroke="#f9d800" stroke-width="2.5"/></svg>Warranty On Parts &amp; Labour</li>
    <li><svg width="14" height="12" viewBox="0 0 14 12"><path d="M1 6l4 4 8-9" fill="none" stroke="#f9d800" stroke-width="2.5"/></svg>Availiable on 24/7</li>
  </ul>
  <div class="btn btn-yellow">Contact Us</div>
  <div class="form-card">
    <h2>Request Services</h2>
    <div class="field" style="left:22px;top:108px;width:173px">Name:</div>
    <div class="field" style="left:207px;top:108px;width:173px">Address:</div>
    <div class="field" style="left:22px;top:155px;width:173px">City:</div>
    <div class="field" style="left:207px;top:155px;width:173px">Zip:</div>
    <div class="field" style="left:22px;top:202px;width:173px">Phone:</div>
    <div class="field" style="left:207px;top:202px;width:173px">Email:</div>
    <div class="field area" style="left:22px;top:250px;width:358px">Comments:</div>
    <svg class="abs" style="left:342px;top:398px" width="20" height="20" viewBox="0 0 24 24"><path d="M2 21 23 12 2 3v7l15 2-15 2z" fill="#1f3a6b"/></svg>
  </div>
  <div class="dots">
    <i style="width:20px;height:20px;background:var(--yellow)"></i>
    <i style="width:8px;height:8px;border:1px solid #fff"></i>
    <i style="width:8px;height:8px;border:1px solid #fff"></i>
  </div>
</section>

<section class="services">
  <h2 class="center-title">More of what<br>you need</h2>
  <div class="underline"></div>
  <div class="arrow light" style="left:74px;top:299px"><svg width="10" height="12" viewBox="0 0 10 12"><path d="M7 1 2 6l5 5" fill="none" stroke="#1f3a6b" stroke-width="2.5"/></svg></div>
  <div class="svc active" style="left:126px"><svg width="36" height="36" viewBox="0 0 24 24"><path d="M14 3l4 4-3 3-4-4zM11 6l-8 8v4h4l8-8" fill="none" stroke="#1f3a6b" stroke-width="2"/></svg>Plumbing</div>
  <div class="svc" style="left:286px"><svg width="26" height="36" viewBox="0 0 16 24"><rect x="2" y="1" width="12" height="18" rx="3" fill="#1f3a6b"/><circle cx="8" cy="8" r="2" fill="#fff"/><path d="M5 20v3M11 20v3" stroke="#1f3a6b" stroke-width="2"/></svg>Water<br>Heaters</div>
  <div class="svc" style="left:447px"><svg width="22" height="36" viewBox="0 0 14 24"><path d="M7 2a2.5 2.5 0 0 1 2.5 2.5V15a4.5 4.5 0 1 1-5 0V4.5A2.5 2.5 0 0 1 7 2z" fill="none" stroke="#1f3a6b" stroke-width="2"/><circle cx="7" cy="18.5" r="2.3" fill="#1f3a6b"/></svg>Heating</div>
  <div class="svc" style="left:608px"><svg width="40" height="36" viewBox="0 0 28 24"><rect x="1" y="3" width="26" height="8" rx="1.5" fill="#1f3a6b"/><path d="M8 14v7M12 14v8M16 14v8M20 14v7" stroke="#1f3a6b" stroke-width="1.5"/></svg>Air<br>Conditioning</div>
  <div class="svc" style="left:769px"><svg width="40" height="36" viewBox="0 0 28 24"><path d="M2 8h16a3 3 0 1 0-3-3M2 13h22a3 3 0 1 1-3 3M2 18h10" fill="none" stroke="#1f3a6b" stroke-width="2"/></svg>Indoor Air<br>Quality</div>
  <div class="svc" style="left:930px"><svg width="36" height="36" viewBox="0 0 24 24"><circle cx="12" cy="12" r="10" fill="none" stroke="#1f3a6b" stroke-width="2"/><path d="M12 5c3 4 4 6 4 8a4 4 0 0 1-8 0c0-2 1-4 4-8z" fill="#1f3a6b"/></svg>Water<br>Filtration</div>
  <div class="arrow dark" style="left:1092px;top:299px"><svg width="10" height="12" viewBox="0 0 10 12"><path d="M3 1l5 5-5 5" fill="none" stroke="#fff" stroke-width="2.5"/></svg></div>
  <div class="btn btn-navy">See More</div>
</section>

<section class="difference">
  <h2>The RK difference<br>makers</h2>
  <div class="underline"></div>
  <p>RK is a favorite choice among homeowners who appreciate our extensive range of home comfort and related services. Others like us best for our 100% satisfaction guarantee, while still others enjoy the many benefits that membership in our Preferred Service Club provides. Add it all up, and there's a lot to like about RK Plumbing, Heating, AC &amp; Remodeling.</p>
  <div class="btn btn-yellow">Learn More</div>
  <div class="circle-bg"></div>
  <svg class="abs" style="left:700px;top:320px" width="500" height="380" viewBox="0 0 500 380"><path d="M10 300c80 80 260 60 330-60C400 140 420 40 500 30" fill="none" stroke="#1f3a6b" stroke-width="2" stroke-dasharray="7 7"/></svg>
  <div class="img-fill" role="img" aria-label="Smiling plumber in navy overalls holding a pipe wrench" style="left:720px;top:100px;width:320px;height:482px;border-radius:160px 160px 20px 20px;background:linear-gradient(180deg,#3a5a92,#1f3a6b)"></div>
  <div class="img-fill" role="img" aria-label="White service van with yellow stripe" style="left:452px;top:438px;width:270px;height:200px;border-radius:30px 60px 20px 20px;background:linear-gradient(180deg,#ffffff,#e4e4e4 70%,#f9d800 70%,#f9d800 78%,#bdbdbd 78%)"></div>
</section>

<section class="savings">
  <h2 class="center-title">Enjoy the savings...<br>plus the added<br>comfort</h2>
  <div class="underline"></div>
  <div class="arrow light" style="left:74px;top:499px"><svg width="10" height="12" viewBox="0 0 10 12"><path d="M7 1 2 6l5 5" fill="none" stroke="#1f3a6b" stroke-width="2.5"/></svg></div>
  <div class="deal" style="left:159px;top:365px;width:261px;height:289px"><div class="img-fill" role="img" aria-label="Outdoor air conditioning unit" style="left:30px;top:40px;width:200px;height:200px;border-radius:6px;background:linear-gradient(180deg,#9a9a9a,#5a5a5a)"></div></div>
  <div class="deal" style="left:436px;top:327px;width:328px;height:367px"><span class="abs" style="left:14px;top:14px;width:34px;height:34px;border-radius:50%;background:#f5f5f5;font-size:5px;font-weight:600;display:flex;align-items:center;justify-content:center;text-align:center;line-height:1.1">NEW<br>ARRIVAL</span><div class="img-fill" role="img" aria-label="Wall-mounted electric water heater" style="left:64px;top:30px;width:200px;height:310px;border-radius:90px 90px 40px 40px;background:linear-gradient(180deg,#f2f2f4,#d6d6dc 70%,#4a5aa8 70%)"></div></div>
  <div class="deal" style="left:781px;top:365px;width:261px;height:289px"><div class="img-fill" role="img" aria-label="Cartoon plumber with a wrench" style="left:70px;top:40px;width:120px;height:200px;border-radius:50px;background:linear-gradient(180deg,#e8d2b8,#3d6fc4 45%,#2a55a8)"></div></div>
  <div class="arrow dark" style="left:1092px;top:499px"><svg width="10" height="12" viewBox="0 0 10 12"><path d="M3 1l5 5-5 5" fill="none" stroke="#fff" stroke-width="2.5"/></svg></div>
  <div class="save"><b>SAVE $120</b><i class="bar"></i><small>On a new water heater,<br>tank-style or tankless.</small></div>
  <div class="btn btn-navy">Click for Details</div>
</section>

<section class="blog">
  <h2>Our latest blog</h2>
  <div class="underline"></div>
  <div class="btn btn-yellow">View All</div>
  <div class="post featured" style="left:126px" role="img" aria-label="Plumber at work behind a navy overlay"><div class="img-fill" style="inset:0;background:linear-gradient(180deg,#4b628c,#1f3a6b)"></div><div class="title">Tab Service</div><p>Lorem Ipsum is simply dummy text of the printing and typesetting</p><div class="more">READ MORE</div></div>
  <div class="post" style="left:367px"><div class="img-fill" role="img" aria-label="Worker jetting a sewer drain" style="inset:0;background:linear-gradient(180deg,#7d8ea8,#2c3a52)"></div><div class="title">Sewer Cleaning</div></div>
  <div class="post" style="left:609px"><div class="img-fill" role="img" aria-label="Hands tightening a pipe with a wrench" style="inset:0;background:linear-gradient(180deg,#c9c9c9,#6e5a50)"></div><div class="title">Pipe Repairing</div></div>
  <div class="post" style="left:850px"><div class="img-fill" role="img" aria-label="White sink drain pipe" style="inset:0;background:linear-gradient(180deg,#d7a86a,#8e6a48)"></div><div class="title">Sink Installation</div></div>
</section>

<section class="reminder">
  <h2 class="center-title">Back to school reminder</h2>
  <div class="underline"></div>
  <p>Most families see an uptick in morning "rush hour" activity once the school year begins, and so does your water heater. Can yours keep up with the increased demand? Contact us today for a water heater check-up and free quote on a replacement system.</p>
</section>

<footer class="footer">
  <div class="logo"><span class="mark"></span><span class="name">RK Plumbing</span></div>
  <p class="about">Lorem Ipsum is simply dummy text of the printing and typesetting industry. Lorem Ipsum has been the industry's standard dummy text ever since the 1500s, when an unknown printer took a galley of type and scrambled it to make</p>
  <i class="vline" style="left:455px"></i>
  <ul class="links"><li>About</li><li>Plumbing</li><li>Water Heaters</li><li>Heating</li><li>Air Conditioning</li><li>Indoor Air Quality</li><li>Commercial</li><li>Handy Work &amp; Remodeling</li></ul>
  <i class="vline" style="left:726px"></i>
  <div class="contact">
    <div class="row"><svg height="30" viewBox="0 0 24 24"><path d="M6.6 10.8a15 15 0 0 0 6.6 6.6l2.2-2.2a1 1 0 0 1 1-.25 11 11 0 0 0 3.6.6 1 1 0 0 1 1 1V20a1 1 0 0 1-1 1A17 17 0 0 1 3 4a1 1 0 0 1 1-1h3.5a1 1 0 0 1 1 1 11 11 0 0 0 .6 3.6 1 1 0 0 1-.25 1z" fill="#f9d800"/></svg><span>555.310.2846<br>555.800.1937</span></div>
    <div class="row" style="align-items:center"><svg height="24" viewBox="0 0 30 20"><rect x="1" y="1" width="28" height="18" fill="none" stroke="#f9d800" stroke-width="2"/><path d="M1 1l14 11L29 1" fill="none" stroke="#f9d800" stroke-width="2"/></svg><span>info@rkplumbing-example.com</span></div>
    <div class="row"><svg height="34" viewBox="0 0 24 24"><path d="M12 2a7 7 0 0 0-7 7c0 5 7 13 7 13s7-8 7-13a7 7 0 0 0-7-7zm0 9.5A2.5 2.5 0 1 1 12 6.5a2.5 2.5 0 0 1 0 5z" fill="#f9d800"/></svg><span>41 Orchard Ave, Suite 120, Fairview<br>NJ 07000</span></div>
    <div class="row" style="align-items:center"><svg height="30" viewBox="0 0 24 24"><circle cx="12" cy="12" r="7" fill="#f9d800"/></svg><span>Social page</span></div>
  </div>
  <i class="copyline"></i>
  <div class="copy">© RK Plumbing 2023. All Rights Reserved.</div>
</footer>

</body>
</html>
```